Banner Ad Design Project for responsive website

Looking to update the main banner on my website www.bridalpathly.com but it will be for our new responsive website, you can see here http://www.bridalpathly.com/dev/
Banner should be 300 px high by1920 pix wide
Please contact me with any questions
Should include:
All the text from the existing banner ie
Bridal Show
THE FIRST 50 BRIDES WILL GET A CHANCE TO WIN $25000
Honeymoon Cruise Giveaway
"Pick the Perfect Gown" casting call
Banner should be 1920 pix wide
Final delivery will require layered psd file and all fonts

Target Market(s)

Brides

Industry/Entity Type

Call

Requirements
Must have
• All the text from the existing banner ie
• Bridal Show
• THE FIRST 50 BRIDES WILL GET A CHANCE TO WIN $25000
• Honeymoon Cruise Giveaway
• "Pick the Perfect Gown" casting call
• Banner should be 1920 pix wide
Nice to have
• The look and feel of our postcard, see attached
Should not have
• Any specifics to any date/time/location as the banner will be online all the time and the specifics for each show will be different

```html
<!DOCTYPE html>
<html lang="en">
<head>
<meta charset="utf-8">
<title>Bridal Show Banner</title>
<link href="https://fonts.googleapis.com/css2?family=Great+Vibes&family=Arimo:wght@400;700&display=swap" rel="stylesheet">
<style>
  :root {
    --page: #efe9e2;
    --banner: #ffffff;
    --green: #1f7a1f;
    --green-deep: #0f6a12;
    --ink: #111111;
    --swirl: #f4f7ea;
    --swirl-grey: #f1f1ef;
    --bell: #edf5ea;
    --sea: #2b5f9c;
    --sky: #a9d3f0;
    --grass: #4f9b2c;
    --gown: #f4f1ee;
    --curve: #b9b9b9;
  }
  html, body {
    margin: 0;
    width: 1200px;
    height: 900px;
    overflow: hidden;
    background: var(--page);
  }
  .banner {
    position: absolute;
    left: 20px;
    top: 240px;
    width: 1160px;
    height: 420px;
    background: var(--banner);
    overflow: hidden;
    box-shadow: 0 4px 18px rgba(0,0,0,0.18);
    font-family: "Arimo", Arial, sans-serif;
  }
  .swirl {
    position: absolute;
    background: var(--swirl);
  }
  .swirl--left {
    left: 0; top: 0; width: 270px; height: 150px;
    border-radius: 0 0 140px 0;
  }
  .swirl--right {
    left: 660px; top: 0; width: 240px; height: 420px;
    background: var(--swirl-grey);
    border-radius: 120px 0 0 120px;
  }
  .bells {
    position: absolute;
    background: var(--bell);
    border-radius: 18px;
  }
  .bells--left { left: 200px; top: 8px; width: 96px; height: 80px; }
  .bells--right { left: 748px; top: 2px; width: 54px; height: 58px; }
  .title {
    position: absolute;
    left: 0; width: 1046px; top: 26px;
    text-align: center;
    font-family: "Great Vibes", cursive;
    font-size: 92px;
    line-height: 1;
    color: var(--green);
    margin: 0;
    font-weight: 400;
  }
  .subtitle {
    position: absolute;
    left: 0; width: 1046px;
    text-align: center;
    color: var(--ink);
    font-size: 30px;
    line-height: 1;
    margin: 0;
  }
  .subtitle--casting { top: 127px; }
  .subtitle--gown { top: 174px; }
  .script {
    font-family: "Great Vibes", cursive;
    color: var(--green);
    font-size: 42px;
  }
  .offer {
    position: absolute;
    left: 0; width: 1046px; top: 256px;
    text-align: center;
    color: var(--ink);
    font-size: 45px;
    line-height: 49px;
    margin: 0;
    text-transform: uppercase;
  }
  .offer strong {
    color: var(--green-deep);
    font-weight: 700;
  }
  .offer .prize {
    display: block;
    font-size: 48px;
    font-weight: 700;
    color: var(--green-deep);
  }
  .giveaway {
    position: absolute;
    left: 0; top: 140px;
    width: 190px;
    text-align: center;
    font-family: "Great Vibes", cursive;
    color: var(--green);
    font-size: 25px;
    line-height: 1;
    white-space: nowrap;
  }
  .giveaway__label { display: block; }
  .giveaway__photo {
    display: block;
    width: 174px; height: 125px;
    margin: 6px 0 14px;
    border-radius: 0 8px 8px 0;
    background: linear-gradient(180deg, var(--sky) 0%, #dfeef8 45%, var(--sea) 62%, #16406f 100%);
  }
  .giveaway__label--end { font-size: 30px; }
  .bride {
    position: absolute;
    right: 0; top: 0;
    width: 300px; height: 420px;
  }
</style>
</head>
<body>
  <section class="banner">
    <div class="swirl swirl--left" role="img" aria-label="Faint green floral swirl ornament"></div>
    <div class="swirl swirl--right" role="img" aria-label="Grey and green floral swirl ornament"></div>
    <div class="bells bells--left" role="img" aria-label="Wedding bells outline ornament"></div>
    <div class="bells bells--right" role="img" aria-label="Wedding bell outline ornament"></div>

    <h1 class="title">Bridal Show</h1>
    <p class="subtitle subtitle--casting">Casting Call</p>
    <p class="subtitle subtitle--gown">Pick the <span class="script">Perfect</span> <span class="script">Gown</span></p>

    <p class="offer">The first <strong>50</strong> brides will<br>get a chance to win<span class="prize">$25,000</span></p>

    <div class="giveaway">
      <span class="giveaway__label">Honeymoon Cruise</span>
      <span class="giveaway__photo" role="img" aria-label="Photo of a cruise ship sailing on the ocean"></span>
      <span class="giveaway__label giveaway__label--end">Giveaway</span>
    </div>

    <svg class="bride" viewBox="0 0 300 420" role="img" aria-label="Photo of a smiling bride in a white gown and veil holding a pink rose bouquet on a green lawn">
      <defs>
        <linearGradient id="bride-fill" x1="0" y1="0" x2="1" y2="1">
          <stop offset="0" stop-color="#6fb13c"/>
          <stop offset="0.45" stop-color="#e9e5e1"/>
          <stop offset="0.8" stop-color="var(--gown)"/>
          <stop offset="1" stop-color="var(--grass)"/>
        </linearGradient>
      </defs>
      <path d="M40 0 H300 V420 H30 C10 340 6 200 40 0 Z" fill="url(#bride-fill)"/>
      <path d="M40 0 C6 200 10 340 30 420" fill="none" stroke="var(--curve)" stroke-width="5"/>
    </svg>
  </section>
</body>
</html>
```